Pellham Ridge Nectar Company, local Honey producer needs product Lable to encourage sales

We are a small business (Pellham Ridge Nectar Company) located in a small Texas town that harvests honey from our beehives yearly. Our honey would be considered "raw wildflower honey" and our goal is to sell it locally (farmers markets) and to surrounding areas.

We are currently packaging in plastic classic honey bottles with white flip caps. Sizes are 8oz and 16oz bottles (see pictures for actual size). Larger orders will be filled in one quart mason jars.

Design Ideas:
-vintage style design with bee or several bees in background
- incorporate company name "Pellham Ridge Nectar Company"
- needs small description "Raw Honey", and "Harvested in Bellville, Texas"

Target Market(s)

Farmers markets, health conscience people looking for unprocessed food options

Industry/Entity Type

Small Business

Requirements
Nice to have
• Vintage feel
Should not have
• No cartoonish characters

```html
<!DOCTYPE html>
<html lang="en">
<head>
<meta charset="utf-8">
<title>Pellham Ridge Nectar Company – Raw Honey Label</title>
<link rel="stylesheet" href="https://fonts.googleapis.com/css2?family=Pinyon+Script&family=Rye&family=Righteous&display=swap">
<style>
  :root {
    --backdrop: #232323;
    --label: #ffffff;
    --honey-green: #1f6f56;
    --honey-green-deep: #175c47;
    --ink: #1b1b1b;
    --ornament: #ececec;
  }
  html, body {
    margin: 0;
    padding: 0;
    width: 735px;
    height: 1200px;
    overflow: hidden;
    background: var(--backdrop);
  }
  .label-canvas {
    display: block;
    width: 735px;
    height: 1200px;
  }
  .label-body { fill: var(--label); }
  .sunburst line {
    stroke: var(--honey-green);
    stroke-width: 3;
    vector-effect: non-scaling-stroke;
  }
  .badge-top { fill: var(--honey-green); }
  .badge-bottom { fill: var(--honey-green-deep); }
  .ornament { fill: var(--ornament); }
  .bee-mark { fill: var(--label); }
  .maker-name {
    font-family: "Pinyon Script", cursive;
    font-size: 31px;
    fill: var(--label);
  }
  .product-name {
    font-family: "Rye", serif;
    font-size: 92px;
    fill: var(--ink);
  }
  .origin-line {
    font-family: "Righteous", sans-serif;
    font-size: 23px;
    fill: var(--ink);
    letter-spacing: 0.5px;
  }
</style>
</head>
<body>
<svg class="label-canvas" viewBox="0 0 735 1200" xmlns="http://www.w3.org/2000/svg">
  <defs>
    <radialGradient id="flourish-tone" cx="50%" cy="50%" r="50%">
      <stop offset="0%" stop-color="#e9e9e9"/>
      <stop offset="100%" stop-color="#ffffff" stop-opacity="0"/>
    </radialGradient>
    <path id="maker-arc" d="M 168 462 Q 367 352 572 470"/>
  </defs>

  <!-- Label shape -->
  <rect class="label-body" x="39" y="28" width="657" height="1145" rx="328.5" ry="328.5"/>

  <!-- Decorative flourish areas -->
  <ellipse role="img" aria-label="Vintage scroll flourish ornament" cx="367" cy="200" rx="300" ry="150" fill="url(#flourish-tone)"/>
  <rect class="ornament" role="img" aria-label="Small scroll ornament" x="112" y="975" width="72" height="72" rx="30" opacity="0.7"/>
  <rect class="ornament" role="img" aria-label="Small scroll ornament" x="551" y="975" width="72" height="72" rx="30" opacity="0.7"/>

  <!-- Sunburst rays -->
  <g class="sunburst" transform="translate(367 607) scale(0.95 1.1)">
    <line x1="0" y1="-345" x2="0" y2="-285"/>
    <line x1="0" y1="-345" x2="0" y2="-300" transform="rotate(7.5)"/>
    <line x1="0" y1="-340" x2="0" y2="-285" transform="rotate(15)"/>
    <line x1="0" y1="-345" x2="0" y2="-305" transform="rotate(22.5)"/>
    <line x1="0" y1="-340" x2="0" y2="-285" transform="rotate(30)"/>
    <line x1="0" y1="-345" x2="0" y2="-300" transform="rotate(37.5)"/>
    <line x1="0" y1="-340" x2="0" y2="-290" transform="rotate(45)"/>
    <line x1="0" y1="-345" x2="0" y2="-305" transform="rotate(52.5)"/>
    <line x1="0" y1="-340" x2="0" y2="-290" transform="rotate(60)"/>
    <line x1="0" y1="-345" x2="0" y2="-305" transform="rotate(67.5)"/>
    <line x1="0" y1="-340" x2="0" y2="-300" transform="rotate(75)"/>
    <line x1="0" y1="-345" x2="0" y2="-315" transform="rotate(82.5)"/>
    <line x1="0" y1="-340" x2="0" y2="-310" transform="rotate(90)"/>
    <line x1="0" y1="-345" x2="0" y2="-315" transform="rotate(97.5)"/>
    <line x1="0" y1="-340" x2="0" y2="-300" transform="rotate(105)"/>
    <line x1="0" y1="-345" x2="0" y2="-305" transform="rotate(112.5)"/>
    <line x1="0" y1="-340" x2="0" y2="-290" transform="rotate(120)"/>
    <line x1="0" y1="-345" x2="0" y2="-305" transform="rotate(127.5)"/>
    <line x1="0" y1="-340" x2="0" y2="-290" transform="rotate(135)"/>
    <line x1="0" y1="-345" x2="0" y2="-300" transform="rotate(142.5)"/>
    <line x1="0" y1="-340" x2="0" y2="-285" transform="rotate(150)"/>
    <line x1="0" y1="-345" x2="0" y2="-305" transform="rotate(157.5)"/>
    <line x1="0" y1="-340" x2="0" y2="-285" transform="rotate(165)"/>
    <line x1="0" y1="-345" x2="0" y2="-300" transform="rotate(172.5)"/>
    <line x1="0" y1="-345" x2="0" y2="-285" transform="rotate(180)"/>
    <line x1="0" y1="-345" x2="0" y2="-300" transform="rotate(187.5)"/>
    <line x1="0" y1="-340" x2="0" y2="-285" transform="rotate(195)"/>
    <line x1="0" y1="-345" x2="0" y2="-305" transform="rotate(202.5)"/>
    <line x1="0" y1="-340" x2="0" y2="-285" transform="rotate(210)"/>
    <line x1="0" y1="-345" x2="0" y2="-300" transform="rotate(217.5)"/>
    <line x1="0" y1="-340" x2="0" y2="-290" transform="rotate(225)"/>
    <line x1="0" y1="-345" x2="0" y2="-305" transform="rotate(232.5)"/>
    <line x1="0" y1="-340" x2="0" y2="-290" transform="rotate(240)"/>
    <line x1="0" y1="-345" x2="0" y2="-305" transform="rotate(247.5)"/>
    <line x1="0" y1="-340" x2="0" y2="-300" transform="rotate(255)"/>
    <line x1="0" y1="-345" x2="0" y2="-315" transform="rotate(262.5)"/>
    <line x1="0" y1="-340" x2="0" y2="-310" transform="rotate(270)"/>
    <line x1="0" y1="-345" x2="0" y2="-315" transform="rotate(277.5)"/>
    <line x1="0" y1="-340" x2="0" y2="-300" transform="rotate(285)"/>
    <line x1="0" y1="-345" x2="0" y2="-305" transform="rotate(292.5)"/>
    <line x1="0" y1="-340" x2="0" y2="-290" transform="rotate(300)"/>
    <line x1="0" y1="-345" x2="0" y2="-305" transform="rotate(307.5)"/>
    <line x1="0" y1="-340" x2="0" y2="-290" transform="rotate(315)"/>
    <line x1="0" y1="-345" x2="0" y2="-300" transform="rotate(322.5)"/>
    <line x1="0" y1="-340" x2="0" y2="-285" transform="rotate(330)"/>
    <line x1="0" y1="-345" x2="0" y2="-305" transform="rotate(337.5)"/>
    <line x1="0" y1="-340" x2="0" y2="-285" transform="rotate(345)"/>
    <line x1="0" y1="-345" x2="0" y2="-300" transform="rotate(352.5)"/>
  </g>

  <!-- Hexagonal badge -->
  <path class="badge-top" d="M 165 420 Q 165 404 180 397 L 350 314 Q 367 306 384 314 L 555 397 Q 570 404 570 420 L 570 548 L 165 548 Z"/>
  <path class="badge-bottom" d="M 165 671 L 570 671 L 570 785 Q 570 796 560 802 L 377 908 Q 367 914 357 908 L 175 802 Q 165 796 165 785 Z"/>

  <!-- Bee emblem area -->
  <rect class="bee-mark" role="img" aria-label="White bee silhouette with spread wings" x="312" y="448" width="110" height="400" rx="55"/>

  <!-- Maker name along the badge crest -->
  <text class="maker-name">
    <textPath href="#maker-arc" startOffset="50%" text-anchor="middle">Pellham Ridge Nectar Company</textPath>
  </text>

  <!-- Product name -->
  <text class="product-name" x="367" y="645" text-anchor="middle" textLength="515" lengthAdjust="spacingAndGlyphs">RAW HONEY</text>

  <!-- Origin -->
  <text class="origin-line" x="367" y="992" text-anchor="middle">HARVESTED IN BELLVILLE</text>
  <text class="origin-line" x="367" y="1030" text-anchor="middle">TEXAS</text>
</svg>
</body>
</html>
```